VORLEN Website Design

We need a website designed for our company VORLEN. We are a luxury lifestyle club that will provide benefits and services for our members. The site should be clean & sleek, preferably using black and white (or darker colors). (example sites: brimvale.example, tusko.example)

Here is a link of a sample page I did using wix. (https://pelmundry4.sitebuild.example/mypage) This can be used to get a general idea.

Target Market(s)

Upper Middle Class in the United States

Number of Pages Required

5+ page

Font styles to use
Sans Serif
Other font styles liked:
• Arial (or other similar fonts)

Requirements
Must have
• A clean design that is eye-catching and speaks to our company.
Nice to have
• Ideas for copy.

```html
<!DOCTYPE html>
<html lang="en">
<head>
<meta charset="utf-8">
<title>VORLEN — Services and Benefits</title>
<link href="https://fonts.googleapis.com/css2?family=Montserrat:wght@400;500;600;700&display=swap" rel="stylesheet">
<style>
  :root {
    --navy-deep: #090e1b;
    --navy: #0c1222;
    --white: #ffffff;
    --text-soft: #e6e8ee;
    --panel-light: #e4e4e4;
    --ink: #14161c;
    --label-band: rgba(18, 22, 32, 0.86);
    --rule: rgba(255, 255, 255, 0.75);
  }
  * { box-sizing: border-box; margin: 0; padding: 0; }
  html, body {
    width: 1077px; height: 1200px; overflow: hidden;
    font-family: "Montserrat", Arial, sans-serif;
    background: var(--navy-deep);
  }
  .page { position: relative; width: 1077px; height: 1200px; }

  /* Header */
  .site-header {
    position: absolute; left: 0; top: 0; width: 1077px; height: 70px;
    background: var(--navy-deep);
    border-bottom: 1px solid var(--rule);
  }
  .brand {
    position: absolute; left: 134px; top: 22px;
    font-size: 27px; font-weight: 400; letter-spacing: 1px;
    color: var(--white);
  }
  .main-nav a {
    position: absolute; top: 32px;
    font-size: 11px; font-weight: 400; letter-spacing: 0.4px;
    color: var(--text-soft); text-decoration: none;
  }
  .main-nav a.is-current { font-weight: 700; color: var(--white); }

  /* Hero */
  .hero {
    position: absolute; left: 0; top: 71px; width: 1077px; height: 387px;
    background: radial-gradient(ellipse at 30% 40%, #111a2e 0%, var(--navy) 55%, var(--navy-deep) 100%);
  }
  .hero-photo {
    position: absolute; left: 134px; top: 69px; width: 334px; height: 250px;
    background: linear-gradient(160deg, #7cc4e6 0%, #5fb2d8 20%, #9c8a6a 45%, #1fb3c4 60%, #0f8fa8 100%);
    box-shadow: 0 4px 14px rgba(0,0,0,0.5);
  }
  .hero-copy { position: absolute; left: 508px; top: 97px; width: 420px; color: var(--white); }
  .hero-copy h1 { font-size: 24px; font-weight: 700; line-height: 30px; }
  .hero-copy p {
    font-size: 12px; line-height: 20px; letter-spacing: 1px;
    color: var(--text-soft); margin-top: 11px;
  }
  .hero-copy p + p { margin-top: 20px; }
  .apply-button {
    position: absolute; left: 0; top: 231px; width: 128px; height: 39px;
    border: 2px solid var(--white); border-radius: 20px;
    display: flex; align-items: center; justify-content: center;
    font-size: 12px; font-weight: 600; color: var(--white);
  }

  /* Services */
  .services {
    position: absolute; left: 0; top: 458px; width: 1077px; height: 675px;
    background: var(--panel-light);
  }
  .services h2 {
    position: absolute; left: 0; top: 32px; width: 1077px; text-align: center;
    font-size: 24px; font-weight: 500; color: var(--ink);
  }
  .service-grid {
    position: absolute; left: 278px; top: 89px;
    display: grid; grid-template-columns: repeat(3, 168px);
    grid-auto-rows: 168px; column-gap: 14px; row-gap: 21px;
  }
  .service-card {
    position: relative; overflow: hidden;
    box-shadow: 0 3px 8px rgba(0,0,0,0.3);
  }
  .service-photo { position: absolute; inset: 0; }
  .service-label {
    position: absolute; left: 0; bottom: 0; width: 100%; height: 36px;
    background: var(--label-band); color: var(--white);
    display: flex; align-items: center; justify-content: center;
    font-size: 12px; font-weight: 500; letter-spacing: 1px;
  }
  .photo-accounting { background: linear-gradient(140deg, #d9d6d2, #a9a6a3 60%, #6a6866); }
  .photo-investment { background: linear-gradient(160deg, #5a5452, #2d2f3a 50%, #8e9296); }
  .photo-lawyer { background: linear-gradient(150deg, #4a3a2c, #3b3d45 50%, #6b5a4c); }
  .photo-realestate { background: linear-gradient(120deg, #f1efec, #d8cbb5 60%, #c2986a); }
  .photo-concierge { background: linear-gradient(170deg, #2a1c14, #6b3f22 50%, #8a5530); }
  .photo-jet { background: linear-gradient(180deg, #1c2f5c, #3c5a8e 55%, #a9b4c4); }
  .photo-events { background: linear-gradient(170deg, #d59a4f, #7b4a1c 50%, #241308); }
  .photo-private { background: linear-gradient(170deg, #5a4236, #8a6a5e 50%, #3d3434); }
  .photo-experiences { background: linear-gradient(160deg, #6f8a5a, #5c8a8e 50%, #2a3440); }

  /* Footer */
  .site-footer {
    position: absolute; left: 0; top: 1133px; width: 1077px; height: 67px;
    background: var(--navy-deep); text-align: center;
  }
  .site-footer h3 {
    margin-top: 13px; font-size: 11px; font-weight: 700; color: var(--white);
    letter-spacing: 0.3px;
  }
  .social-links { display: flex; justify-content: center; gap: 10px; margin-top: 7px; }
  .social-dot { width: 13px; height: 13px; border-radius: 50%; background: #c7c9cf; }
</style>
</head>
<body>
<div class="page">
  <header class="site-header">
    <div class="brand">VORLEN</div>
    <nav class="main-nav">
      <a href="#" style="left:549px">HOME</a>
      <a href="#" style="left:610px">ABOUT</a>
      <a href="#" class="is-current" style="left:676px">SERVICES AND BENEFITS</a>
      <a href="#" style="left:853px">APPLY</a>
      <a href="#" style="left:914px">CONTACT</a>
    </nav>
  </header>

  <section class="hero">
    <div class="hero-photo" role="img" aria-label="Turquoise bay below rocky cliffs with a busy beach"></div>
    <div class="hero-copy">
      <h1>We Are VORLEN</h1>
      <p>Built in the image of a "Multi-Family Office", VORLEN provides members with access to just about any service, experience, and event desirable.</p>
      <p>VORLEN is truly the most exclusive lifestyle club out</p>
      <a class="apply-button" href="#">Apply</a>
    </div>
  </section>

  <section class="services">
    <h2>Services and Benefits</h2>
    <div class="service-grid">
      <div class="service-card"><div class="service-photo photo-accounting" role="img" aria-label="Hand signing a financial document"></div><div class="service-label">Accounting Services</div></div>
      <div class="service-card"><div class="service-photo photo-investment" role="img" aria-label="Laptop showing an analytics dashboard"></div><div class="service-label">Investment Services</div></div>
      <div class="service-card"><div class="service-photo photo-lawyer" role="img" aria-label="Business handshake across a desk"></div><div class="service-label">Lawyer Services</div></div>
      <div class="service-card"><div class="service-photo photo-realestate" role="img" aria-label="House keys being handed over"></div><div class="service-label">Real Estate Services</div></div>
      <div class="service-card"><div class="service-photo photo-concierge" role="img" aria-label="Latte beside a service bell on a wooden counter"></div><div class="service-label">24/7 Concierge</div></div>
      <div class="service-card"><div class="service-photo photo-jet" role="img" aria-label="Aircraft wing above the clouds"></div><div class="service-label">Private Jet Travel</div></div>
      <div class="service-card"><div class="service-photo photo-events" role="img" aria-label="Concert crowd in warm stage light"></div><div class="service-label">Event Access</div></div>
      <div class="service-card"><div class="service-photo photo-private" role="img" aria-label="Guests gathered at an evening party"></div><div class="service-label">Private Events</div></div>
      <div class="service-card"><div class="service-photo photo-experiences" role="img" aria-label="Sneakers dangling high above a coastline"></div><div class="service-label">Experiences</div></div>
    </div>
  </section>

  <footer class="site-footer">
    <h3>CONTACT US</h3>
    <div class="social-links">
      <span class="social-dot"></span><span class="social-dot"></span><span class="social-dot"></span><span class="social-dot"></span><span class="social-dot"></span>
    </div>
  </footer>
</div>
</body>
</html>
```